Tidy Acres Complete Garden & Lawn Care

I will upload a flyer, I wanna pretty much same, please change the logo and I will upload description of the job I offer soon
Gonna be in A5 size, and I would like like double sides
I would like something creative and modern to impress the clients, I upload my business card as well, on flyer need to have my business card information
BRILKOR IS ONLY A SAMPLE FLYER AND PLEASE I DONT WANT TO SEE IT IN MY FLYERS, Thanks
Updates
on small lines instead of 6 months I would like 3 months
Target Market(s)
Residentials and commercials
Industry/Entity Type
Business
Look and feel
Each slider illustrates characteristics of the customer's brand and the style your logo design should communicate.

```html
<!DOCTYPE html>
<html lang="en">
<head>
<meta charset="utf-8">
<title>Tidy Acres – Lawn Mowing Flyer</title>
<link rel="stylesheet" href="https://fonts.googleapis.com/css2?family=Catamaran:wght@600;700;800&family=Hind:wght@600;700&display=swap">
<style>
  :root {
    --forest: #2d5e33;
    --deep: #0b6434;
    --leaf: #8ab93d;
    --leaf-dark: #2f6b30;
    --white: #ffffff;
    --silver: #cfd3d0;
  }
  * { margin: 0; padding: 0; box-sizing: border-box; }
  html, body { width: 846px; height: 1200px; overflow: hidden; background: var(--white); }
  .flyer {
    position: relative;
    width: 846px;
    height: 1200px;
    overflow: hidden;
    background: var(--forest);
    font-family: "Catamaran", "Hind", sans-serif;
    color: var(--white);
  }
  .flyer__backdrop { position: absolute; inset: 0; }

  .brand {
    position: absolute;
    left: 48px; top: 70px;
    width: 460px;
    text-align: center;
    color: var(--forest);
    font-weight: 700;
  }
  .brand__mark {
    width: 120px; height: 120px;
    margin: 0 auto 18px;
    border-radius: 50%;
    background: var(--forest);
  }
  .brand__name { font-size: 56px; line-height: 1; letter-spacing: 4px; text-transform: uppercase; }
  .brand__tagline { margin-top: 10px; font-size: 21px; letter-spacing: 2px; text-transform: uppercase; }

  .badge { position: absolute; left: 520px; top: 180px; width: 310px; height: 280px; }

  .offer {
    position: absolute;
    left: 0; right: 0; top: 484px;
    text-align: center;
  }
  .offer__headline {
    font-weight: 800;
    font-size: 58px;
    line-height: 52px;
    letter-spacing: -0.5px;
  }
  .offer__rule {
    width: 758px; height: 4px;
    margin: 22px auto 14px 42px;
    background: var(--white);
    border: 0;
  }
  .offer__guarantee { font-weight: 700; font-size: 36px; line-height: 40px; }
  .accent { color: var(--leaf); }

  .services {
    position: absolute;
    left: 46px; top: 744px;
    width: 754px; height: 236px;
    padding-top: 10px;
    background: var(--leaf);
    border: 2px solid var(--white);
    border-radius: 12px;
    list-style: none;
    text-align: center;
    color: var(--leaf-dark);
    font-family: "Hind", sans-serif;
    font-weight: 600;
    font-size: 26px;
    line-height: 36px;
  }

  .contact {
    position: absolute;
    left: 40px; top: 1004px;
    width: 762px; height: 156px;
    padding-top: 8px;
    background: var(--deep);
    border: 3px dashed var(--white);
    border-radius: 12px;
    text-align: center;
    font-weight: 700;
    font-size: 36px;
    line-height: 44px;
  }
</style>
</head>
<body>
<main class="flyer">
  <svg class="flyer__backdrop" width="846" height="1200" viewBox="0 0 846 1200" aria-hidden="true">
    <path d="M0,0 H804 C745,210 560,445 0,474 Z" fill="var(--leaf)"/>
    <path d="M0,0 H742 C690,170 540,392 0,426 Z" fill="var(--white)"/>
  </svg>

  <header class="brand">
    <div class="brand__mark"></div>
    <div class="brand__name">Tidy Acres</div>
    <div class="brand__tagline">Complete Garden &amp; Lawn Care</div>
  </header>

  <svg class="badge" viewBox="0 0 310 280" role="img" aria-label="Best value guaranteed">
    <path d="M40,10 H270 Q280,10 280,20 V170 Q280,230 155,272 Q30,230 30,170 V20 Q30,10 40,10 Z"
          fill="var(--white)" stroke="var(--silver)" stroke-width="6"/>
    <path d="M46,22 H264 V168 Q264,218 155,256 Q46,218 46,168 Z" fill="none" stroke="var(--forest)" stroke-width="3"/>
    <text x="155" y="92" text-anchor="middle" font-family="Catamaran, sans-serif" font-weight="800" font-size="66" fill="var(--forest)">BEST</text>
    <text x="155" y="160" text-anchor="middle" font-family="Catamaran, sans-serif" font-weight="800" font-size="60" fill="var(--forest)">VALUE</text>
    <g transform="rotate(-9 155 210)">
      <rect x="4" y="180" width="302" height="58" rx="29" fill="var(--white)" stroke="var(--silver)" stroke-width="5"/>
      <text x="155" y="224" text-anchor="middle" font-family="Catamaran, sans-serif" font-weight="800" font-size="38" fill="var(--forest)">GUARANTEED</text>
    </g>
  </svg>

  <section class="offer">
    <h1 class="offer__headline">We’ll beat your current<br>lawn mowing rate by <span class="accent">10%</span></h1>
    <hr class="offer__rule">
    <p class="offer__guarantee">New price guaranteed for <span class="accent">3 months!</span></p>
  </section>

  <ul class="services">
    <li>Residential &amp; Commercial - Obligation free quotes</li>
    <li>Complete lawn &amp; garden care - garden spraying</li>
    <li>Weed spraying,&nbsp; landscaping, Mulching</li>
    <li>High pressure cleaning - Gutter &amp; paths</li>
    <li>Section cleaning - Property vacates</li>
    <li>Trailer loads - General handyman Jobs</li>
  </ul>

  <address class="contact" style="font-style: normal;">
    <div class="contact__names">Daniel/Marcus</div>
    <div class="contact__phone">phone: 0400 555 274</div>
    <div class="contact__email">email: admin@tidyacres.com.au</div>
  </address>
</main>
</body>
</html>
```